Create modern and sleek business card for luxury real estate company

We're a "boutique" real estate office looking for a design that gets across a highly modern luxury brand. Blacks and whites are probably the best colors unless we try a silver foil for the logo. I've attached a version of our current logo here. I'd like to swap out the current font on there with Gotham Light Regular.

I'm looking to have one side of the card have the logo with the space for our agents info on the other side.

Target Market(s)

Young professionals in a "luxury" headspace

Industry/Entity Type

Real estate

Contact Information for Business Card

A place for agent name, cell number, website. The slogan "Simply Rethinking Real Estate".

Font styles to use
Other font styles liked:
• Gotham Regular

Colors

Designer to choose only greyscale colors for use in the design.

Requirements
Must have
• Matte black as the background color. Clean lines and use of contrast. A specific design aspect that will use silver foil.
Nice to have
• Up in the air on integrating a QR code
Should not have
• Any houses or other real estate related design (ex: a clip art house)

```html
<!DOCTYPE html>
<html lang="en">
<head>
<meta charset="utf-8">
<title>Halden Estates – Business Card</title>
<link rel="stylesheet" href="https://fonts.googleapis.com/css2?family=Montserrat:wght@300;400&display=swap">
<style>
  :root {
    --page-bg: #e9eae9;
    --card-white: #ffffff;
    --ink: #1a1a1a;
    --matte-black: #161616;
    --silver: #c9c9c9;
    --silver-light: #f4f4f4;
    --silver-dark: #8e8e8e;
  }
  * { margin: 0; padding: 0; box-sizing: border-box; }
  html, body {
    width: 1200px; height: 900px; overflow: hidden;
    background: var(--page-bg);
    font-family: "Montserrat", sans-serif;
    color: var(--ink);
  }
  .stage {
    position: relative; width: 1200px; height: 900px;
    display: flex; align-items: center; justify-content: center; gap: 40px;
  }
  .card {
    position: relative; width: 540px; height: 309px;
    box-shadow: 0 8px 24px rgba(0,0,0,0.18);
    overflow: hidden;
  }
  /* Front: agent details */
  .card-front { background: var(--card-white); }
  .brand {
    position: absolute; left: 58px; top: 92px;
    display: flex; align-items: center; gap: 16px;
  }
  .brand-mark {
    width: 66px; height: 66px; border-radius: 50%;
    border: 3px solid var(--ink);
  }
  .brand-name {
    font-weight: 400; font-size: 27px; line-height: 0.95;
    letter-spacing: 1px; text-transform: uppercase;
  }
  .contact-list {
    position: absolute; left: 100px; top: 186px;
    list-style: none; font-weight: 300; font-size: 11.5px; letter-spacing: 0.8px;
  }
  .contact-item {
    display: flex; align-items: center; gap: 10px; height: 21px;
  }
  .contact-icon { width: 14px; height: 14px; flex: none; }
  .contact-dash { width: 12px; text-align: center; }

  /* Back: brand side */
  .card-back { background: var(--matte-black); }
  .foil-band { position: absolute; top: 0; height: 100%; width: 70px; }
  .foil-band-left { left: 0; }
  .foil-band-right { right: 0; }
  .back-emblem {
    position: absolute; left: 50%; top: 50%;
    width: 196px; height: 196px; transform: translate(-50%, -50%);
    border-radius: 50%; border: 5px solid var(--silver);
    display: flex; align-items: center; justify-content: center;
  }
  .back-name {
    color: var(--silver); font-weight: 400; font-size: 20px;
    letter-spacing: 2px; line-height: 1.2; text-align: center; text-transform: uppercase;
  }
</style>
</head>
<body>
<main class="stage">
  <section class="card card-front" aria-label="Card front with agent details">
    <div class="brand">
      <span class="brand-mark"></span>
      <p class="brand-name">Halden<br>Estates</p>
    </div>
    <ul class="contact-list">
      <li class="contact-item">
        <svg class="contact-icon" viewBox="0 0 14 14"><rect x="1.5" y="1.5" width="11" height="11" rx="3" fill="none" stroke="var(--ink)" stroke-width="1.6"/></svg>
        <span class="contact-dash">-</span><span>Agent Photo Feed</span>
      </li>
      <li class="contact-item">
        <svg class="contact-icon" viewBox="0 0 14 14"><rect x="1.5" y="1.5" width="11" height="11" rx="3" fill="none" stroke="var(--ink)" stroke-width="1.6"/></svg>
        <span class="contact-dash">-</span><span>Agent Video Channel</span>
      </li>
      <li class="contact-item">
        <svg class="contact-icon" viewBox="0 0 14 14"><circle cx="7" cy="7" r="5.5" fill="none" stroke="var(--ink)" stroke-width="1.6"/></svg>
        <span class="contact-dash">-</span><span>Agent Social Page</span>
      </li>
      <li class="contact-item">
        <svg class="contact-icon" viewBox="0 0 14 14"><path d="M3.2 1.8 L5.4 1.8 L6.3 4.6 L4.9 5.6 C5.6 7.2 6.8 8.4 8.4 9.1 L9.4 7.7 L12.2 8.6 L12.2 10.8 C12.2 11.6 11.6 12.2 10.8 12.2 C6 12 2 8 1.8 3.2 C1.8 2.4 2.4 1.8 3.2 1.8 Z" fill="none" stroke="var(--ink)" stroke-width="1.3" stroke-linejoin="round"/></svg>
        <span class="contact-dash">-</span><span>90909XXXXX</span>
      </li>
      <li class="contact-item">
        <svg class="contact-icon" viewBox="0 0 14 14"><rect x="1" y="3" width="12" height="8.5" fill="none" stroke="var(--ink)" stroke-width="1.6"/><path d="M1.5 3.5 L7 8 L12.5 3.5" fill="none" stroke="var(--ink)" stroke-width="1.3"/></svg>
        <span class="contact-dash">-</span><span>agent@haldenestates.com</span>
      </li>
    </ul>
  </section>

  <section class="card card-back" aria-label="Card back with brand name">
    <svg class="foil-band foil-band-left" viewBox="0 0 70 309" preserveAspectRatio="none" aria-hidden="true">
      <defs>
        <linearGradient id="foilLeft" x1="0" y1="0" x2="1" y2="0">
          <stop offset="0" stop-color="var(--silver-dark)"/>
          <stop offset="0.45" stop-color="var(--silver-light)"/>
          <stop offset="1" stop-color="var(--silver)"/>
        </linearGradient>
      </defs>
      <path d="M0 0 H28 Q62 18 62 60 V249 Q62 291 28 309 H0 Z" fill="url(#foilLeft)"/>
    </svg>
    <svg class="foil-band foil-band-right" viewBox="0 0 70 309" preserveAspectRatio="none" aria-hidden="true">
      <defs>
        <linearGradient id="foilRight" x1="1" y1="0" x2="0" y2="0">
          <stop offset="0" stop-color="var(--silver-dark)"/>
          <stop offset="0.45" stop-color="var(--silver-light)"/>
          <stop offset="1" stop-color="var(--silver)"/>
        </linearGradient>
      </defs>
      <path d="M70 0 H42 Q8 18 8 60 V249 Q8 291 42 309 H70 Z" fill="url(#foilRight)"/>
    </svg>
    <div class="back-emblem">
      <p class="back-name">Halden<br>Estates</p>
    </div>
  </section>
</main>
</body>
</html>
```